New startup requiring business card

New company needed a business card / logo. Company name is
Minthel
Company is providing IT software sales, partnering and consulting services across the APAC region. Catch line is "growing together".
We currently have a feeling yellow as the primary colour given its meaning across the region but open to ideas. Main brief is we want something smart, clean and professional while still leveraging the strength of the name.
A major part of the business is mutually beneficial partnerships, not sure if this helps but maybe visual around linkages between objects.
Also wanting a standard size card, preference is something that will have a D/S cello sheen finish in a matt. But again open to ideas, wow us!
Software

```html
<!DOCTYPE html>
<html lang="en">
<head>
<meta charset="utf-8">
<title>Minthel — Business Card</title>
<link rel="stylesheet" href="https://fonts.googleapis.com/css2?family=Roboto:wght@400;700&display=swap">
<style>
  :root {
    --canvas: #d9d9d9;
    --card-dark: #101010;
    --card-dark-glow: #1c1c1c;
    --card-light: #f1f1f1;
    --card-light-glow: #fbfbfb;
    --ink-dark: #2a2a2a;
    --ink-mid: #555555;
    --ink-soft: #808080;
    --ink-white: #ffffff;
    --accent: #f2d800;
    --divider: #d2d2d2;
  }
  * { margin: 0; padding: 0; box-sizing: border-box; }
  html, body {
    width: 1200px; height: 1200px; overflow: hidden;
    background: var(--canvas);
    font-family: "Roboto", Arial, sans-serif;
  }
  .canvas {
    width: 1200px; height: 1200px;
    display: flex; flex-direction: column; align-items: center; justify-content: center;
    gap: 60px;
  }
  .card {
    width: 840px; height: 480px;
    position: relative;
    box-shadow: 0 10px 30px rgba(0,0,0,0.18);
  }
  .card--back {
    background: radial-gradient(ellipse at 50% 40%, var(--card-dark-glow), var(--card-dark) 70%);
    display: flex; align-items: center; justify-content: center;
  }
  .card--front {
    background: radial-gradient(ellipse at 35% 35%, var(--card-light-glow), var(--card-light) 75%);
    display: flex; align-items: center;
  }
  .brand { display: flex; align-items: center; gap: 14px; }
  .brand__square { width: 26px; height: 26px; background: var(--accent); }
  .brand__name {
    font-weight: 700; font-size: 46px; letter-spacing: 1px; text-transform: uppercase; line-height: 1;
  }
  .card--back .brand__name { color: var(--ink-white); }
  .card--front .brand__name { color: var(--ink-dark); }

  .front__brand {
    width: 45%; height: 360px;
    display: flex; align-items: center; justify-content: center;
    border-right: 1px solid var(--divider);
  }
  .front__details { padding-left: 48px; }
  .person__name { font-weight: 700; font-size: 38px; color: var(--ink-dark); line-height: 1.15; }
  .person__title { font-size: 21px; color: var(--ink-mid); margin-top: 4px; }
  .contact { margin-top: 26px; display: grid; grid-template-columns: 86px 1fr; row-gap: 4px; font-size: 15px; color: var(--ink-soft); }
  .contact dt, .contact dd { line-height: 1.35; }
</style>
</head>
<body>
<main class="canvas">
  <section class="card card--back" aria-label="Card back">
    <div class="brand">
      <span class="brand__square"></span>
      <span class="brand__name">Minthel</span>
    </div>
  </section>

  <section class="card card--front" aria-label="Card front">
    <div class="front__brand">
      <div class="brand">
        <span class="brand__square"></span>
        <span class="brand__name">Minthel</span>
      </div>
    </div>
    <div class="front__details">
      <h1 class="person__name">Soren Vale</h1>
      <p class="person__title">Executive Creative Director</p>
      <dl class="contact">
        <dt>Phone</dt><dd>: +888 4170 395</dd>
        <dt>Mail</dt><dd>: soren@minthel.net</dd>
        <dt>Website</dt><dd>: http://minthel.net/</dd>
        <dt>Address</dt><dd>: Orrin Street 212 Block C<br>&nbsp;&nbsp;Fenwick City - Arden</dd>
      </dl>
    </div>
  </section>
</main>
</body>
</html>
```